Brand new redesign of Brightwell finance website

I need a new website design that i can advertise a great low interest rate on the front page and capture input application details that will send through to my email address.

some car finance companies will be similar to this would be listed below

tallyfunds.com.au
corelinefinance.com.au
finance715.com.au
wexburyfinance.com.au
finance93.com.au

Reason: I have changed the project to a committed project. all the webpages should have the same format just different content and i want to be able to edit the front page easily to update my interest rates.

Reason: Provide more time for resubmission and submission work

Target Market(s)

Australian Finance market targeting a younger demographic

Industry/Entity Type

Finance

Coding

Coded - Design and coding required

Number of Pages Required

5+ page

Font styles to use
Serif
Sans Serif

Colors
0255a3
ffffff
cedeed

Requirements
Must have
• application capture form
• apply now buttons
• Headline rate front page

```html
<!DOCTYPE html>
<html lang="en">
<head>
<meta charset="utf-8">
<title>Brightwell Finance</title>
<link href="https://fonts.googleapis.com/css2?family=Lato:wght@400;700;900&family=Signika:wght@400;600;700&display=swap" rel="stylesheet">
<style>
:root{
  --blue:#0255a3;
  --blue-dark:#0a3f7d;
  --pale:#cedeed;
  --white:#ffffff;
  --ink:#231f20;
  --text:#333333;
  --field:#f1f1f1;
  --grey:#4a4a4a;
  --brand:#4f86d6;
}
*{margin:0;padding:0;box-sizing:border-box}
html,body{width:813px;height:1200px;overflow:hidden;background:var(--white)}
body{position:relative;font-family:'Lato',sans-serif;color:var(--text)}
.abs{position:absolute}
.heading{font-family:'Signika',sans-serif}

/* top bar */
.topbar{left:0;top:0;width:813px;height:22px;background:var(--blue)}
.apply-btn{left:641px;top:0;width:83px;height:22px;background:var(--pale);color:var(--blue);font-size:8.5px;display:flex;align-items:center;justify-content:center;gap:5px;text-decoration:none}
.header{left:0;top:22px;width:813px;height:80px;background:var(--ink)}
.brand{left:88px;top:64px;display:flex;align-items:center;gap:6px;color:var(--brand);font-weight:700;font-size:14px;line-height:14px;letter-spacing:.5px}
.brand-dot{width:12px;height:12px;border-radius:50%;background:var(--brand);flex:none}
.phone{left:558px;top:42px;color:#d6d6d6;font-size:10px;display:flex;align-items:center;gap:5px}
.social{display:flex;gap:5px}
.social span{width:19px;height:19px;border-radius:3px;background:#3b6fc2;display:block}
.header-social{left:656px;top:40px}
.nav{left:226px;top:72px;display:flex;font-size:9px;font-weight:700;color:var(--white);letter-spacing:.2px}
.nav a{color:var(--white);text-decoration:none;padding:5px 10px;height:19px;display:flex;align-items:center}
.nav a.active{background:var(--blue)}

/* hero */
.hero-photo{left:0;top:102px;width:813px;height:317px;background:linear-gradient(100deg,#c9c2b8 0%,#b7a898 30%,#d2c6b6 55%,#b69c86 80%,#9c8e84 100%)}
.promo{left:90px;width:228px;height:38px;background:rgba(40,40,40,.78);color:var(--white);font-size:12px;padding:0 11px;display:flex;flex-direction:column;justify-content:center;line-height:16px;border-radius:2px}
.dots{left:385px;top:399px;display:flex;gap:6px}
.dots span{width:6px;height:6px;border-radius:50%;background:rgba(255,255,255,.45)}
.dots span.on{background:transparent;border:1.5px solid var(--blue)}

.quick-form{left:514px;top:126px;width:210px;height:268px;background:var(--white);box-shadow:0 1px 4px rgba(0,0,0,.25)}
.quick-form h2{height:31px;margin-top:3px;background:var(--blue);color:var(--white);font-size:15px;font-weight:700;padding-left:9px;line-height:31px;letter-spacing:.2px}
.field-label{position:absolute;left:8px;font-size:8px;color:#444}
.field{position:absolute;left:8px;width:194px;height:22px;background:var(--field);border:1px solid #e2e2e2}
.select{font-size:8px;color:#444;padding-left:6px;line-height:20px}
.select svg{position:absolute;right:8px;top:8px}
.submit{position:absolute;left:8px;top:234px;width:70px;height:22px;background:var(--grey);color:var(--white);font-size:10.5px;font-weight:700;font-family:'Signika',sans-serif;display:flex;align-items:center;justify-content:center;letter-spacing:.4px}

/* pre approval */
.section-title{color:var(--blue);font-size:19px;font-weight:600;letter-spacing:.6px}
.pre-title{left:90px;top:442px}
.rule{height:1px;background:#c6d6e8}
.pre-text{left:90px;top:484px;width:310px;font-size:8.7px;line-height:14.1px;color:#333}
.pre-bold{left:90px;top:577px;width:310px;font-size:8.7px;line-height:14px;font-weight:700;color:#222}
.pre-call{left:90px;top:613px;font-size:11.5px;color:#222}
.pre-call strong{color:var(--blue);font-size:13px;margin-left:4px}

.tile{width:141px;background:var(--blue);color:var(--white);display:flex;flex-direction:column;align-items:center;font-family:'Signika',sans-serif;font-weight:600;font-size:11.5px;letter-spacing:.4px}
.tile .icon{width:42px;height:42px;border-radius:50%;background:var(--white);display:flex;align-items:center;justify-content:center}

/* promo halves */
.calc-photo{left:0;top:656px;width:406px;height:202px;background:linear-gradient(135deg,#2f6fb8,#1c5aa6 50%,#3a7cc4)}
.approval-photo{left:406px;top:656px;width:407px;height:202px;background:linear-gradient(120deg,#4b4b4b,#6e6a66 45%,#3a3a3a)}
.promo-block{color:var(--white);text-align:center}
.promo-block h3{font-family:'Signika',sans-serif;font-size:16.5px;font-weight:600;line-height:23px;letter-spacing:.6px}
.promo-block p{font-size:11.3px;line-height:17px;margin-top:9px}
.pill{position:absolute;height:24px;border-radius:12px;background:rgba(255,255,255,.92);color:var(--blue);font-size:10.5px;font-weight:700;display:flex;align-items:center;gap:8px;padding-left:5px}
.pill i{width:17px;height:17px;border-radius:50%;background:#aab8c8;display:block}

/* solutions */
.solutions-title{left:0;width:813px;top:880px;text-align:center}
.service{left:378px;font-family:'Signika',sans-serif;font-size:11px;font-weight:600;color:#222;letter-spacing:.5px}

/* contact */
.contact-band{left:0;top:1051px;width:813px;height:93px;background:var(--pale)}
.contact{display:flex;gap:8px;color:#222}
.contact .ic{width:23px;height:23px;border-radius:50%;background:var(--blue);display:flex;align-items:center;justify-content:center;margin-top:-2px}
.contact b{display:block;font-size:10px;font-weight:700;margin-bottom:4px}
.contact span{font-size:10px}
.divider{width:1px;height:64px;top:1072px;background:var(--white)}

/* footer */
.footer{left:0;top:1144px;width:813px;height:56px;background:var(--blue)}
.foot-nav{left:90px;top:1157px;display:flex;gap:11px;font-size:7.6px;color:var(--white);letter-spacing:.5px}
.copyright{left:90px;top:1175px;font-size:7.6px;font-weight:700;color:var(--white);letter-spacing:.4px}
.footer-social{left:656px;top:1162px}
.footer-social span{background:#3d78cc}
</style>
</head>
<body>

<div class="abs topbar"></div>
<a class="abs apply-btn" href="#">
  <svg width="10" height="11" viewBox="0 0 10 11"><path d="M1 .5h5.5L9 3v7.5H1z" fill="none" stroke="#222"/><path d="M3 5h4M3 7h4M3 9h3" stroke="#222"/></svg>
  Apply Now
</a>

<header class="abs header"></header>
<div class="abs brand"><span class="brand-dot"></span><span>BRIGHTWELL<br>FINANCE</span></div>
<div class="abs phone">
  <svg width="13" height="13" viewBox="0 0 24 24"><path d="M6.6 10.8a15 15 0 0 0 6.6 6.6l2.2-2.2a1 1 0 0 1 1-.25 11.4 11.4 0 0 0 3.6.57 1 1 0 0 1 1 1V20a1 1 0 0 1-1 1A17 17 0 0 1 3 4a1 1 0 0 1 1-1h3.5a1 1 0 0 1 1 1c0 1.25.2 2.45.57 3.57a1 1 0 0 1-.25 1z" fill="none" stroke="#bbb" stroke-width="1.6"/></svg>
  1300 555 246
</div>
<div class="abs social header-social" role="img" aria-label="Social media links"><span></span><span></span><span></span></div>
<nav class="abs nav">
  <a class="active" href="#">HOME</a><a href="#">ABOUT</a><a href="#">VEHICLE LOANS</a><a href="#">OTHER LOANS</a><a href="#">INSURANCE</a><a href="#">FINANCE CALCULATOR</a><a href="#">CONTACT</a>
</nav>

<div class="abs hero-photo" role="img" aria-label="Photo of a smiling family relaxing together on a sofa at home"></div>
<div class="abs promo" style="top:256px">LOW RATE CAR LOANS FROM 4.69%<br>COMPARISON RATE 4.99%</div>
<div class="abs promo" style="top:307px">LOW FEES</div>
<div class="abs promo" style="top:358px">LOW TOTAL COST LOANS</div>
<div class="abs dots"><span></span><span class="on"></span><span></span><span></span></div>

<form class="abs quick-form">
  <h2 class="heading">LET'S GET STARTED NOW!</h2>
  <div class="field-label" style="top:47px">Loan Amount</div>
  <div class="field" style="top:63px"></div>
  <div class="field-label" style="top:92px">Deposit (if Any)</div>
  <div class="field" style="top:108px"></div>
  <div class="field-label" style="top:136px">Purpose of Loan</div>
  <div class="field select" style="top:152px">Car<svg width="10" height="6"><path d="M0 0h10L5 6z" fill="#444"/></svg></div>
  <div class="field-label" style="top:181px">Postal Code</div>
  <div class="field" style="top:196px"></div>
  <div class="submit">SUBMIT</div>
</form>

<h2 class="abs section-title heading pre-title">ONLINE LOAN PRE APPROVAL</h2>
<div class="abs rule" style="left:90px;top:470px;width:306px"></div>
<p class="abs pre-text">Lorem ipsum dolor sit amet, consectetuer adipiscing elit, sed dia nonummy laoreet dolore magna aliquam erat volutpat. Ut wisi enim ad minim veniam, quis nostrud exerci tation ullamcorper suscipit lobortis nisl ut aliquip ex eaLorem ipsum dolor sit amet, consectetuer adipiscing elit, sed dia nonummy laoreet dolore magna aliquam erat volutpat. Ut wisi enim ad minim veniam, quis nostrud exerci tation ullamcorper suscipit lobortis</p>
<p class="abs pre-bold">Lorem ipsum dolor sit amet, consectetuer adipiscing elit, sed dia nonummy laoreet dolore magna aliquam erat volutpat.</p>
<p class="abs pre-call">Fill Out Our Quick Form Below or <strong>Call 1300 555 246</strong></p>

<div class="abs tile" style="left:429px;top:446px;height:87px;padding-top:11px">
  <span class="icon"><svg width="22" height="16" viewBox="0 0 22 16"><path d="M4 6l2-4h10l2 4h2v6h-2v3h-3v-3H7v3H4v-3H2V6z" fill="var(--blue)"/><rect x="5" y="7" width="3" height="2" fill="#fff"/><rect x="14" y="7" width="3" height="2" fill="#fff"/></svg></span>
  <span style="margin-top:10px">VEHICLE LOANS</span>
</div>
<div class="abs tile" style="left:582px;top:446px;height:87px;padding-top:11px">
  <span class="icon"><svg width="22" height="18" viewBox="0 0 22 18"><path d="M7 2h8v4H7z" fill="var(--blue)"/><path d="M2 8h18l-3 6H5z" fill="var(--blue)"/><path d="M1 16q5-2 10 0t10 0" stroke="var(--blue)" stroke-width="1.5" fill="none"/></svg></span>
  <span style="margin-top:10px">BOAT LOANS</span>
</div>
<div class="abs tile" style="left:429px;top:544px;height:86px;padding-top:12px">
  <span class="icon"><svg width="22" height="20" viewBox="0 0 22 20"><path d="M11 1L1 10h3v9h5v-6h4v6h5v-9h3z" fill="var(--blue)"/></svg></span>
  <span style="margin-top:11px">HOME LOANS</span>
</div>
<div class="abs tile" style="left:582px;top:544px;height:86px;padding-top:12px">
  <span class="icon"><svg width="18" height="20" viewBox="0 0 18 20"><circle cx="9" cy="5" r="4" fill="var(--blue)"/><path d="M1 19c0-6 3-9 8-9s8 3 8 9z" fill="var(--blue)"/></svg></span>
  <span style="margin-top:11px">PERSONAL LOANS</span>
</div>

<div class="abs calc-photo" role="img" aria-label="Photo of hands working on a calculator with paperwork, in a blue tint"></div>
<div class="abs promo-block" style="left:0;width:384px;top:686px">
  <h3>WHAT WILL<br>MY REPAYMENTS BE?</h3>
  <p>See How Much You Could Borrow With<br>Our Loan Calculator</p>
</div>
<a class="pill" style="left:122px;top:786px;width:138px">
  <i></i>LOAN CALCULATOR</a>

<div class="abs approval-photo" role="img" aria-label="Photo of a young woman sitting on the bonnet of a new car"></div>
<div class="abs promo-block" style="left:406px;width:407px;top:693px">
  <h3>FIND OUT WHAT GUARANTEED<br>APPROVAL ACTUALLY MEANS</h3>
  <p>We Explain What it Means and<br>What We Offer Instead</p>
</div>
<a class="pill" style="left:542px;top:793px;width:131px;gap:18px">
  <i></i>FIND OUT MORE</a>

<h2 class="abs section-title heading solutions-title">BRIGHTWELL SOLUTIONS</h2>
<div class="abs rule" style="left:254px;top:912px;width:304px"></div>
<svg class="abs" style="left:210px;top:930px" width="170" height="100" viewBox="0 0 170 100">
  <circle cx="52" cy="52" r="44" fill="none" stroke="var(--blue)" stroke-width="3"/>
  <g stroke="#3aa0e0" stroke-width=".8" stroke-dasharray="1.5 1.5" fill="none">
    <path d="M98 52L160 16"/><path d="M98 52L160 40"/><path d="M98 52L160 65"/><path d="M98 52L160 91"/>
  </g>
  <g fill="#3aa0e0"><circle cx="161" cy="16" r="1.8"/><circle cx="161" cy="40" r="1.8"/><circle cx="161" cy="65" r="1.8"/><circle cx="161" cy="91" r="1.8"/></g>
</svg>
<div class="abs service" style="top:939px">BAS AGENT</div>
<div class="abs service" style="top:963px">PAYROLL AND BOOKKEEPING SERVICES</div>
<div class="abs service" style="top:988px">CREDIT FILE REPAIR / DEFAULT REMOVALS</div>
<div class="abs service" style="top:1014px">DEBT CONSOLIDATION</div>

<div class="abs contact-band"></div>
<div class="abs contact" style="left:89px;top:1084px">
  <span class="ic"><svg width="10" height="13" viewBox="0 0 10 13"><path d="M5 0a5 5 0 0 0-5 5c0 3.5 5 8 5 8s5-4.5 5-8a5 5 0 0 0-5-5z" fill="#fff"/><circle cx="5" cy="5" r="1.8" fill="var(--blue)"/></svg></span>
  <div><b>BRIGHTWELL FINANCE</b><span>48 Harbour Lane, Eastwick - 402817</span></div>
</div>
<div class="abs divider" style="left:354px"></div>
<div class="abs contact" style="left:393px;top:1084px">
  <span class="ic"><svg width="11" height="11" viewBox="0 0 24 24"><path d="M6.6 10.8a15 15 0 0 0 6.6 6.6l2.2-2.2a1 1 0 0 1 1-.25 11.4 11.4 0 0 0 3.6.57 1 1 0 0 1 1 1V20a1 1 0 0 1-1 1A17 17 0 0 1 3 4a1 1 0 0 1 1-1h3.5a1 1 0 0 1 1 1c0 1.25.2 2.45.57 3.57a1 1 0 0 1-.25 1z" fill="#fff"/></svg></span>
  <div><b>CALL US</b><span>1300 555 246</span></div>
</div>
<div class="abs divider" style="left:532px"></div>
<div class="abs contact" style="left:571px;top:1084px">
  <span class="ic"><svg width="11" height="8" viewBox="0 0 11 8"><rect width="11" height="8" rx="1" fill="#fff"/><path d="M.5.5l5 4 5-4" stroke="var(--blue)" fill="none"/></svg></span>
  <div><b>EMAIL US</b><span>info@brightwellfinance.com</span></div>
</div>

<footer class="abs footer"></footer>
<div class="abs foot-nav"><span>HOME</span><span>ABOUT</span><span>VEHICLE LOANS</span><span>OTHER LOANS</span><span>INSURANCE</span><span>FINANCE CALCULATOR</span><span>CONTACT</span></div>
<div class="abs copyright">COPYRIGHT © 2016 BRIGHTWELL FINANCE. ALL RIGHTS RESERVED.</div>
<div class="abs social footer-social" role="img" aria-label="Social media links"><span></span><span></span><span></span></div>

</body>
</html>
```